Hemp (cannabis) CBD Oil 3-page Blog website

The objective is 1) to look like professional/serious company, 2) to get investors excited about our Hemp business, 3) to get investor email and phone numbers and build a sense community. Potential investors should become excited that this is their “window of opportunity,” because VeltoriKa is made up of extraordinary people who all have made successful business before, that the location in Uruguay is a huge benefit, that we will become the biggest and best CBD-oil manufacturer in Latin America, and that we focus on all-legal medicinal CBD oil extracted from hemp.

Target Market(s)

Potential investors looking to invest between $30,000-$1,000,000 USD into a HEMP startup business, based in Uruguay, South America.

Industry/Entity Type

Business

Number of Pages Required

3 page

Font styles to use
Sans Serif

Requirements
Must have
• Three pages: Home, Members Only, News (blog).
• FOR MORE DETAIL SEE ATTACHED WORD REQUIREMENTS DOCUMENT.
Nice to have
• Uruguay colors: sky blue, golden sun. Medicinal. Legal. Mainstream. Hemp. Professional people. Opportunity/Money/Investor. Uruguay. Latin America. 1st to Market.
Should not have
• Marijuana (HEMP yes, marijuana NO), anything that looks illegal.

```html
<!DOCTYPE html>
<html lang="en">
<head>
<meta charset="utf-8">
<title>VeltoriKa — Hemp CBD</title>
<link href="https://fonts.googleapis.com/css2?family=Roboto:wght@300;400;500&family=Montserrat:wght@500;700&family=Raleway:wght@400;500;600&display=swap" rel="stylesheet">
<style>
:root{
  --teal:#25b8c4;
  --green:#1bb37c;
  --green-dark:#139061;
  --leaf:#6cc24a;
  --blue:#1b5fae;
  --line:#1aa68a;
  --ink:#222;
  --muted:#555;
  --card-grey:#6b6b6b;
  --field:#7c8f4a;
  --white:#fff;
}
*{box-sizing:border-box;margin:0;padding:0}
html,body{width:1200px;height:2936px;overflow:hidden}
body{position:relative;font-family:'Roboto',sans-serif;color:var(--ink);background:var(--white)}
.abs{position:absolute}

/* nav */
.site-nav{left:0;top:0;width:1200px;height:67px;background:var(--white)}
.brand{left:118px;top:18px;display:flex;align-items:center;gap:8px;font-size:26px;font-weight:400;color:var(--blue)}
.brand-dot{width:14px;height:14px;border-radius:50%;background:var(--leaf)}
.menu{right:0;top:0;height:67px;display:flex;list-style:none;font-size:15px;color:#444}
.menu li{height:67px;line-height:67px;padding:0 11px}
.menu li.active{background:var(--teal);color:var(--white);padding:0 14px}

/* hero */
.hero{left:0;top:67px;width:1200px;height:442px;background:linear-gradient(180deg,#d9e8e0 0%,#8fba86 45%,#4f8a3c 100%)}
.hero-title{left:123px;top:256px;width:415px;height:110px;background:rgba(108,194,74,.9);color:var(--white);padding:10px 14px}
.hero-title .l1{font-size:54px;font-weight:400;line-height:56px}
.hero-title .l2{font-size:36px;font-weight:400;line-height:40px}

/* news bar */
.news-bar{left:0;top:509px;width:1200px;height:96px;background:var(--green)}
.news-label{left:0;top:0;width:303px;height:96px}
.news-label span{position:absolute;left:131px;top:35px;color:var(--white);font-size:22px;font-weight:500}
.news-text{left:315px;top:36px;color:var(--white);font-size:20px}

/* about */
.about{left:0;top:605px;width:1200px;height:550px;background:linear-gradient(180deg,#dfe6d8 0%,#eef1ea 60%,#fff 100%)}
.section-title{width:1200px;left:0;text-align:center;font-size:38px;font-weight:400;color:var(--ink)}
.diagram{left:0;top:0}
.node{font-size:22px;font-weight:400;color:#444;white-space:nowrap}
.about-copy{left:200px;top:1080px;width:800px;text-align:center;font-size:19px;line-height:28px;color:var(--ink)}

/* team */
.team-bg{left:0;top:1155px;width:1200px;height:875px;background:linear-gradient(180deg,#fff 0%,#fff 28%,#a9ad78 52%,#7e8a48 75%,#5e6a33 100%)}
.team-sub{left:260px;top:1254px;width:680px;text-align:center;font-size:16px;line-height:21px;color:var(--muted)}
.card{width:222px;height:318px;background:var(--white);box-shadow:0 2px 6px rgba(0,0,0,.25)}
.card-head{height:222px;background:var(--card-grey);text-align:center;color:var(--white)}
.avatar{width:120px;height:120px;border-radius:50%;margin:24px auto 0;border:2px solid #eee}
.card-name{font-family:'Montserrat',sans-serif;font-weight:700;font-size:15px;margin-top:16px;letter-spacing:.5px}
.card-role{font-family:'Montserrat',sans-serif;font-weight:500;font-size:10px;line-height:14px;margin:6px 12px 0}
.card-bio{padding:16px 16px 0;font-size:10.5px;line-height:14px;text-align:center;color:#444}

/* contact */
.contact-photo{top:2030px;height:574px;background:linear-gradient(180deg,#9cc86e 0%,#4f8b32 60%,#2f5f20 100%)}
.contact-panel{left:257px;top:2030px;width:685px;height:574px;background:rgba(248,250,246,.97);font-family:'Raleway',sans-serif}
.contact-title{left:0;top:42px;width:685px;text-align:center;font-size:27px;font-weight:500;letter-spacing:1px}
.contact-rule{left:278px;top:90px}
.contact-lead{left:100px;top:113px;width:485px;text-align:center;font-size:13px;font-weight:600;line-height:21px}
.contact-phone{left:0;top:168px;width:685px;text-align:center;font-size:12px;line-height:19px;color:#555}
.field{height:34px;border:1px solid #dfe6d8;background:#f6f8f3;font-size:10px;color:#999;padding:10px 10px}
.field sup{color:#6cc24a}
.send{left:0;top:480px;width:685px;text-align:center;font-size:10px;font-weight:600;letter-spacing:1px;color:#6aa53a}

/* map */
.map{left:0;top:2604px;width:1200px;height:332px;background:linear-gradient(90deg,#eceee8 0%,#e7eadf 70%,#a9d0f2 88%,#8cc1ef 100%)}
</style>
</head>
<body>

<header class="site-nav abs">
  <div class="brand abs"><span class="brand-dot"></span>VeltoriKa</div>
  <ul class="menu abs">
    <li class="active">Home</li><li>Members Only</li><li>About</li><li>Team</li><li>News Blog</li><li>Contact</li>
  </ul>
</header>

<section class="hero abs" role="img" aria-label="Photo of hemp plants growing inside a bright greenhouse"></section>
<div class="hero-title abs">
  <div class="l1">Pioneering New</div>
  <div class="l2">Growth Opportunities</div>
</div>

<div class="news-bar abs">
  <svg class="news-label abs" width="303" height="96" viewBox="0 0 303 96"><polygon points="0,0 280,0 303,48 280,96 0,96" fill="#139061"/><text></text></svg>
  <div class="news-label abs"><span>Recent News</span></div>
  <div class="news-text abs">Jan 16, 2017: VeltoriKa awarded $60,000 biotechnology grant by the Uruguayan government.</div>
</div>

<section class="about abs" role="img" aria-label="Faded photo of a grower holding hemp leaves in an open field"></section>
<h2 class="section-title abs" style="top:640px">ABOUT US</h2>
<svg class="diagram abs" width="1200" height="1080" viewBox="0 0 1200 1080">
  <g stroke="#1aa68a" stroke-width="2">
    <line x1="599" y1="752" x2="599" y2="815"/>
    <line x1="599" y1="935" x2="599" y2="1012"/>
    <line x1="464" y1="875" x2="539" y2="875"/>
    <line x1="659" y1="875" x2="736" y2="875"/>
    <line x1="565" y1="925" x2="545" y2="950"/>
    <line x1="633" y1="925" x2="653" y2="950"/>
  </g>
  <circle cx="599" cy="875" r="60" fill="#1b5fae"/>
  <text x="599" y="886" text-anchor="middle" font-family="Roboto,sans-serif" font-size="32" fill="#fff">CBD</text>
</svg>
<div class="node abs" style="left:517px;top:712px">Hemp Cultivation</div>
<div class="node abs" style="left:257px;top:862px">Genetic Engineering</div>
<div class="node abs" style="left:750px;top:862px">Extraction</div>
<div class="node abs" style="left:414px;top:961px">New Markets</div>
<div class="node abs" style="left:658px;top:961px">Oil Refinement</div>
<div class="node abs" style="left:496px;top:1020px">Therapeutic Products</div>
<p class="about-copy abs">Our hemp was enginnered to maximize therapeutic CBD. Under Uruguayan laws we refine the oil at 2x higher profitability than anywhere else in the world.</p>

<section class="team-bg abs" role="img" aria-label="Photo of a hemp field under open sky"></section>
<h2 class="section-title abs" style="top:1198px">OUR TEAM</h2>
<p class="team-sub abs">Our team is composed of experts, each an authority in their field. And each of us has a successful record of starting business.</p>

<article class="card abs" style="left:245px;top:1316px">
  <div class="card-head"><div class="avatar" role="img" aria-label="Portrait photo of Dra. Valeria Montes" style="background:#c9b9a4"></div>
  <div class="card-name">Dra. Valeria Montes</div><div class="card-role">Regulatory Affairs, Import/Export Management, Business Finance</div></div>
  <p class="card-bio">For the past five years, Dr. Montes has been a partner at Norvel Law &amp; Accounting, practicing in the area of business administration</p>
</article>
<article class="card abs" style="left:491px;top:1316px">
  <div class="card-head"><div class="avatar" role="img" aria-label="Portrait photo of Ethan Calder" style="background:#8e7a66"></div>
  <div class="card-name">Ethan Calder</div><div class="card-role">Business Development, Quality Assurance, Operations Management</div></div>
  <p class="card-bio">Mr. Calder has more than 15 years of experience in product engineering, startups and business management in the USA</p>
</article>
<article class="card abs" style="left:736px;top:1316px">
  <div class="card-head"><div class="avatar" role="img" aria-label="Portrait photo of Rafael Quintero" style="background:#5b5450"></div>
  <div class="card-name">Rafael Quintero</div><div class="card-role">Business Development, Strategic Planning</div></div>
  <p class="card-bio">Rafael is a businessman with background in management, negotiations and building of distributor partnerships within the pharmaceutical</p>
</article>
<article class="card abs" style="left:245px;top:1660px">
  <div class="card-head"><div class="avatar" role="img" aria-label="Portrait photo of Tomás Ibarra" style="background:#77706a"></div>
  <div class="card-name">Tomás Ibarra</div><div class="card-role">Plant Genetic Research &amp; Development</div></div>
  <p class="card-bio">Tomás has worked with cannabis plant genetics for 20 years. He is a founding member of the Hemp Research Society of Uruguay</p>
</article>
<article class="card abs" style="left:491px;top:1660px">
  <div class="card-head"><div class="avatar" role="img" aria-label="Portrait photo of Martín Solano among plants" style="background:#6f7a5c"></div>
  <div class="card-name">Martín Solano</div><div class="card-role">Marketing &amp; Communications, Plant Management ???</div></div>
  <p class="card-bio">Martín has 15 years of experience in marketing, merchandising and sales, and 5 years experience in cannabis cultivation. He is president</p>
</article>
<article class="card abs" style="left:736px;top:1660px">
  <div class="card-head"><div class="avatar" role="img" aria-label="Portrait photo of Diego Ferreyra with hemp plants" style="background:#4f7a3c"></div>
  <div class="card-name">Diego Ferreyra</div><div class="card-role">Grow Production Manager, External Affairs</div></div>
  <p class="card-bio">Diego is an authority in the advancement of cannabis research, and has been interviewed and seen on Northwave Television, State</p>
</article>

<section class="contact-photo abs" style="left:0;width:257px" role="img" aria-label="Close-up photo of hemp leaves"></section>
<section class="contact-photo abs" style="left:942px;width:258px;background:linear-gradient(180deg,#8cc4e8 0%,#7fb85a 40%,#3e7428 100%)" role="img" aria-label="Photo of hemp plants against blue sky"></section>
<section class="contact-panel abs">
  <h2 class="contact-title abs">CONTACT</h2>
  <svg class="contact-rule abs" width="130" height="10" viewBox="0 0 130 10"><line x1="0" y1="5" x2="56" y2="5" stroke="#9ccf6e"/><circle cx="65" cy="5" r="4" fill="none" stroke="#9ccf6e"/><line x1="74" y1="5" x2="130" y2="5" stroke="#9ccf6e"/></svg>
  <p class="contact-lead abs">Ut enimex ea ad minim veniam, quis nostrud exercitation ullamco laboris nisi ut aliquip ex ea commodo. Duis aute irure dolor.</p>
  <p class="contact-phone abs">Phone<br>USA (+1) 555 014 2730 &nbsp;UY (+598) 555 018 4620</p>
  <div class="field abs" style="left:35px;top:231px;width:301px">First Name <sup>*</sup></div>
  <div class="field abs" style="left:350px;top:231px;width:301px">Last Name</div>
  <div class="field abs" style="left:35px;top:280px;width:301px">Email <sup>*</sup></div>
  <div class="field abs" style="left:350px;top:280px;width:301px">Subject</div>
  <div class="field abs" style="left:35px;top:329px;width:616px;height:108px">Message <sup>*</sup></div>
  <svg class="abs" style="left:0;top:0" width="685" height="574" viewBox="0 0 685 574">
    <g stroke="#9ccf6e" stroke-width="1.5" fill="none">
      <line x1="270" y1="474" x2="420" y2="474"/>
      <line x1="265" y1="501" x2="425" y2="501"/>
      <line x1="280" y1="462" x2="280" y2="514"/>
      <line x1="405" y1="462" x2="405" y2="514"/>
    </g>
  </svg>
  <div class="send abs">SEND A MESSAGE</div>
</section>

<section class="map abs" role="img" aria-label="Road map of Uruguay and its borders with location pins"></section>

</body>
</html>
```